Brochure

I have a current booklet for Cedar Ridge Labs, I need to incorporate additional information and testing into it. attached are the current inside pages and the additional items that need to be added.

Requirements
Must have
• matching the background, colors, and format of the original inside booklet pages.

```html
<!DOCTYPE html>
<html lang="en">
<head>
<meta charset="utf-8">
<title>Cedar Ridge Labs – Antibiotic Resistance Gene Panel</title>
<link rel="stylesheet" href="https://fonts.googleapis.com/css2?family=Montserrat:wght@400;500;700;800&display=swap">
<style>
  :root {
    --blue: #1f7bc4;
    --blue-mid: #4a8fd1;
    --blue-light: #b9daf3;
    --blue-pale: #e3effa;
    --ink: #1d1d1f;
    --trim: #333335;
    --slate: #55585c;
    --white: #ffffff;
  }
  * { margin: 0; padding: 0; box-sizing: border-box; }
  html, body { width: 982px; height: 1200px; overflow: hidden; background: var(--white); }
  .page {
    position: relative; width: 982px; height: 1200px; overflow: hidden;
    font-family: "Montserrat", sans-serif; color: var(--ink);
  }
  .corner-art { position: absolute; left: 0; top: 0; width: 982px; height: 1200px; }
  .trim-band {
    position: absolute; left: 928px; top: 0; width: 54px; height: 1200px;
    background: var(--trim);
  }
  .trim-note {
    position: absolute; left: 956px; top: 601px;
    transform: translate(-50%, -50%) rotate(90deg);
    white-space: nowrap; color: var(--white);
    font-weight: 700; font-size: 16.5px;
  }
  .page-title {
    position: absolute; left: 162px; top: 132px;
    color: var(--blue); font-weight: 800; font-size: 45px; line-height: 48px;
    letter-spacing: 0.2px;
  }
  .lab-illustration {
    position: absolute; left: 166px; top: 280px; width: 246px; height: 249px;
    border-radius: 12px;
    background: linear-gradient(180deg, var(--blue-pale), var(--blue-light));
  }
  .provider-illustration {
    position: absolute; left: 648px; top: 223px; width: 117px; height: 139px;
    border-radius: 10px;
    background: linear-gradient(180deg, var(--blue-pale), #cfe3f5);
  }
  .targets { position: absolute; left: 512px; top: 388px; width: 390px; text-align: center; }
  .targets h2 { color: var(--blue); font-weight: 800; font-size: 26px; line-height: 30px; }
  .targets p { font-size: 16.5px; line-height: 22px; font-weight: 500; margin-top: 1px; }
  .target-box {
    position: absolute; left: 521px; top: 519px; width: 371px; height: 319px;
    border: 2px solid var(--blue); border-radius: 23px; background: var(--white);
    padding: 19px 0 0 20px;
  }
  .target-box h3 { color: var(--blue); font-weight: 700; font-size: 16.5px; line-height: 20px; }
  .target-list { list-style: none; }
  .target-list li {
    position: relative; padding-left: 27px;
    font-size: 16.5px; line-height: 21.8px; font-weight: 500; white-space: nowrap;
  }
  .target-list li::before { content: "•"; position: absolute; left: 0; font-size: 12px; }
  .feature { position: absolute; left: 164px; display: flex; align-items: center; }
  .feature svg { width: 100px; height: 100px; flex: none; }
  .feature p {
    margin-left: 20px; font-size: 17px; line-height: 22px; font-weight: 500;
  }
  .feature strong { font-weight: 700; }
</style>
</head>
<body>
<div class="page">
  <svg class="corner-art" viewBox="0 0 982 1200" aria-hidden="true">
    <defs>
      <linearGradient id="facetBlue" x1="0.1" y1="1" x2="1" y2="0.1">
        <stop offset="0" stop-color="#b8daf4"/>
        <stop offset="0.45" stop-color="#5da0dc"/>
        <stop offset="0.75" stop-color="#3a72ad"/>
        <stop offset="1" stop-color="#24395a"/>
      </linearGradient>
    </defs>
    <polygon points="438,1143 928,823 928,1040 200,1200" fill="url(#facetBlue)"/>
    <polygon points="173,1200 928,1035 928,1200" fill="var(--slate)"/>
    <text x="889" y="1170" fill="#ffffff" font-family="Montserrat, sans-serif" font-size="12" letter-spacing="1">29</text>
  </svg>

  <div class="trim-band"></div>
  <div class="trim-note">Tabs Here - This portion will be trimmed off</div>

  <h1 class="page-title">ANTIBIOTIC<br>RESIDTANCE GENE</h1>

  <div class="lab-illustration" role="img" aria-label="Illustration of a PCR machine with sample tubes, virus particles and a DNA strand"></div>
  <div class="provider-illustration" role="img" aria-label="Illustration of a healthcare provider wearing a cap with a cross"></div>

  <section class="targets">
    <h2>12 TARGETS</h2>
    <p>A provider’s #1 priority is their patients. When you bring them more targets, you are providing them better tools for treatment</p>
  </section>

  <section class="target-box">
    <h3>ABR</h3>
    <ul class="target-list">
      <li>KPC – Carbapenem resistance</li>
      <li>NDM – Carbapenem resistance</li>
      <li>VIM – Carbapenem resistance</li>
      <li>IMP – Carbapenem resistance</li>
      <li>qnr – Quinolone resistance</li>
      <li>vanB – Vancomycin resistance</li>
      <li>OXA-48 – Carbapenem resistance</li>
      <li>mecA/mecC – Methicillin resistance</li>
      <li>CTX-M ESBL</li>
      <li>sul – Sulfonamide resistance</li>
      <li>vanA – Vancomycin resistance</li>
      <li>dfrA – Trimethoprim resistance</li>
    </ul>
  </section>

  <div class="feature" style="top:590px">
    <svg viewBox="0 0 100 100" aria-hidden="true">
      <circle cx="48" cy="50" r="45" fill="var(--blue-light)" stroke="var(--blue-mid)" stroke-width="4"/>
      <circle cx="48" cy="50" r="35" fill="var(--blue-pale)"/>
      <text x="48" y="70" text-anchor="middle" font-family="Montserrat, sans-serif" font-weight="800" font-size="52" fill="var(--blue-mid)">$</text>
    </svg>
    <p><strong>Cost effective</strong> to help<br>maximize your lab’s<br><strong>profits</strong></p>
  </div>

  <div class="feature" style="top:713px">
    <svg viewBox="0 0 100 100" aria-hidden="true">
      <circle cx="50" cy="50" r="45" fill="var(--blue-light)" stroke="var(--blue-mid)" stroke-width="4"/>
      <circle cx="50" cy="50" r="36" fill="var(--white)" stroke="var(--blue-mid)" stroke-width="3"/>
      <polyline points="60,24 46,50 60,66" fill="none" stroke="var(--blue-mid)" stroke-width="5" stroke-linecap="round"/>
      <polygon points="2,6 24,30 4,32" fill="var(--blue-light)" stroke="var(--blue-mid)" stroke-width="2"/>
    </svg>
    <p><strong>&lt;45 minute</strong> run<br>time ensures <strong>faster</strong><br>turnaround times</p>
  </div>

  <div class="feature" style="top:840px">
    <svg viewBox="0 0 100 100" aria-hidden="true">
      <g fill="var(--blue-light)" stroke="var(--blue-mid)" stroke-width="3">
        <path d="M40,2 h20 l3,13 l11,6 l12,-5 l10,17 l-10,9 v12 l10,9 l-10,17 l-12,-5 l-11,6 l-3,13 h-20 l-3,-13 l-11,-6 l-12,5 l-10,-17 l10,-9 v-12 l-10,-9 l10,-17 l12,5 l11,-6 z"/>
      </g>
      <circle cx="50" cy="50" r="28" fill="var(--blue-pale)" stroke="var(--blue-mid)" stroke-width="3"/>
      <circle cx="50" cy="50" r="12" fill="var(--white)" stroke="var(--blue-mid)" stroke-width="3"/>
    </svg>
    <p>Compatible with <strong>ALL<br>PCR MACHINES</strong></p>
  </div>

  <div class="feature" style="top:970px">
    <svg viewBox="0 0 100 100" aria-hidden="true">
      <g fill="var(--blue-pale)" stroke="var(--blue-mid)" stroke-width="3">
        <rect x="1" y="76" width="18" height="22"/>
        <rect x="28" y="60" width="18" height="38"/>
        <rect x="55" y="40" width="18" height="58"/>
        <rect x="80" y="4" width="18" height="94"/>
      </g>
      <line x1="6" y1="40" x2="42" y2="6" stroke="var(--blue-mid)" stroke-width="5"/>
      <polygon points="26,2 48,0 46,22" fill="var(--blue-mid)"/>
    </svg>
    <p><strong>Highly demanded</strong> targets<br>to make your lab <strong>more<br>appealing to providers</strong></p>
  </div>
</div>
</body>
</html>
```